Cobra Vane Systems Website Revamp

We need a full website for the oil and gas sector to showcase our company and our technology/services we provide to larger corporations. We want our website represent innovation and identity.

Background:

We are a service based company that specializes in:

- well services, and
-permanent applications
**(Please be aware that these are two different aspects to the oil and gas sector, both of which we supply to our customers)

We provide a wide range of jet pump technologies to address under performing reservoirs or problematic well producing conditions. We have field operations currently in: Canada, Oman, and Australia with efforts currently underway to expand in other markets. Therefore are needing a website to help promote a better comprehension of what we do and how we can solve their well issues. We are looking for

1.) Identity;
2.) Emphasis on better comprehension of our services for our clients to relate to us as a solution to their needs;
3.) User friendly interface - but new and exciting in this digital age .

Some examples of websites we like:

http://brindlowinc.com/how-we-work/
http://www.qorvantix.com/qorvan-system/
https://velmorafield.com/

Videos of our technologies:

https://www.clipvarro.com/watch?v=519KdpQWzRe
https://www.clipvarro.com/watch?v=t7NBwuhsp43

Target Market(s)

Petroleum Industry Clients

Coding

Coded - Design and coding required

Number of Pages Required

5+ page

Colors

Designer to choose colors to be used in the design.

Requirements
Must have
• See Project Description, and feel free to contact us with any questions/inquiries!
Nice to have
• Our color scheme is generally 'blue', to depict jet pumps (our service). However, we are open to ideas and artistic interpretation. Grayscale/offset colors/highlight colors etc.

```html
<!DOCTYPE html>
<html lang="en">
<head>
<meta charset="utf-8">
<title>Cobra Vane Systems – The Solution</title>
<link rel="stylesheet" href="https://fonts.googleapis.com/css2?family=Open+Sans:wght@400;700&display=swap">
<style>
  :root {
    --brand-blue: #0a4f94;
    --heading-grey: #5a5a5a;
    --body-grey: #555555;
    --btn-start: #6b97c9;
    --btn-end: #0a2a55;
    --page-bg: #ffffff;
  }
  * { box-sizing: border-box; margin: 0; padding: 0; }
  html, body {
    width: 1200px; height: 1200px; overflow: hidden;
    background: var(--page-bg);
    font-family: "Open Sans", Arial, sans-serif;
    color: var(--body-grey);
  }
  .page { position: relative; width: 1200px; height: 1200px; overflow: hidden; }
  .block { position: absolute; }
  .media { position: absolute; }

  .section-title {
    font-weight: 700; color: var(--heading-grey);
    font-size: 35px; line-height: 38px; letter-spacing: 0.2px;
  }
  .kicker {
    font-weight: 700; color: var(--brand-blue);
    font-size: 50px; line-height: 52px;
  }
  .copy p {
    font-size: 12.8px; line-height: 19.2px; margin-bottom: 19.2px;
    hyphens: auto; -webkit-hyphens: auto; letter-spacing: -0.05px;
  }
  .btn {
    position: absolute; display: flex; align-items: center; justify-content: center;
    width: 171px; height: 37px; border-radius: 19px;
    background: linear-gradient(90deg, var(--btn-start), var(--btn-end));
    color: #fff; font-size: 13px; text-decoration: none; letter-spacing: 0.2px;
  }

  /* Section 1 */
  .wells-art {
    left: 118px; top: 0; width: 394px; height: 334px;
    background: linear-gradient(180deg, #8fd14a 0%, #7fc13c 22%, #cfc6ae 40%, #8d7c66 68%, #2b1612 86%, #d7c2ad 100%);
  }
  .solution { left: 565px; top: -18px; width: 520px; }
  .solution .section-title { margin-top: 4px; }
  .solution .copy { margin-top: 24px; width: 500px; padding-left: 3px; }
  .solution-btn { left: 569px; top: 293px; }

  /* Section 2 */
  .rigless { left: 120px; top: 466px; width: 520px; }
  .rigless .copy { margin-top: 30px; padding-left: 2px; width: 508px; }
  .rigless-btn { left: 123px; top: 835px; }
  .tablet-art {
    left: 650px; top: 452px; width: 462px; height: 346px;
    border-radius: 22px;
    background: linear-gradient(160deg, #7b8082 0%, #5a5f61 55%, #4a4e50 100%);
  }
  .tool-kit-art {
    left: 842px; top: 718px; width: 148px; height: 148px; border-radius: 50%;
    background: linear-gradient(160deg, #f4f4f4 0%, #e4e4e4 100%);
    border: 6px solid #ffffff;
    box-shadow: 0 4px 14px rgba(0,0,0,0.18);
  }

  /* Section 3 */
  .surface-art {
    left: 118px; top: 998px; width: 478px; height: 210px;
    border: 2px solid #cfcfcf; border-radius: 26px 26px 0 0;
    background: linear-gradient(180deg, #f4f4f4 0%, #e7eef6 100%);
  }
  .low-hp { left: 631px; top: 1004px; width: 420px; }
  .low-hp .copy { margin-top: 30px; padding-left: 4px; width: 330px; }
</style>
</head>
<body>
<main class="page">

  <section class="solution-section">
    <div class="media wells-art" role="img" aria-label="Cut-away illustration of an oil well drilling through rock layers into an oil pocket beneath impervious rock"></div>
    <div class="block solution">
      <h1 class="kicker">The Solution</h1>
      <h2 class="section-title">Horizontal &amp; Deviated Wells:</h2>
      <div class="copy">
        <p>With no moving parts, the Cobra Vane jet pump takes the industry to the next level, allowing for jet pump placement anywhere in the horizontal profile. Using power fluid as the drive mechanism of a jet pump, the system has no problems with deviated, crooked or horizontal wellbores.</p>
        <p>With a jet pump landed in the horizontal section of a well, operators are not only able to achieve higher inflow rates, they are also able to achieve higher ultimate reserve recovery</p>
      </div>
    </div>
    <a class="btn solution-btn" href="#">LEARN MORE</a>
  </section>

  <section class="rigless-section">
    <div class="block rigless">
      <h2 class="section-title">Rig-less Pump Changes</h2>
      <div class="copy">
        <p>The heart of the jet pump is a carrier sub which contains the venturi nozzle and throat. If for any reason these parts need to be serviced, retreival is a fast and simple one man operation – done by reversing the system flow direction and reversing the carrier out of the wellbore. Reinstallation is done simply by loading the carrier back into the wellhead and pumping it back into place.</p>
        <p>With the wellhead configured for easy reversing and tool capture – pump inspection, parts replacement or system optimization changes are a one man job, typically performed within a 1 hour service time.</p>
        <p>At Cobra Vane, we have also developed a jet pump cleaning tool, which can be deployed and retrieved in this same manner, allowing us to flush clean the internal components of the jet pump body.</p>
      </div>
    </div>
    <a class="btn rigless-btn" href="#">LEARN MORE</a>
    <div class="media tablet-art" role="img" aria-label="Tablet in a folio stand showing jet pump installation and retrieval animation"></div>
    <div class="media tool-kit-art" role="img" aria-label="Red tool case holding the jet pump carrier and components"></div>
  </section>

  <section class="surface-section">
    <div class="media surface-art" role="img" aria-label="Tablet showing diagrams of flooded vessel and production separator surface package supply layouts"></div>
    <div class="block low-hp">
      <h2 class="section-title">Low HP Requirement<br>Surface Packages</h2>
      <div class="copy">
        <p>Two important factors in this performance are the patented intake flow geometry of the jet pump and the analysis software and techniques employed to optimize the nozzle / throat selection. These two factors have allowed Cobra Vane jet pumps to operate at 50 to 65% efficiency in the field.</p>
      </div>
    </div>
  </section>

</main>
</body>
</html>
```